Harborlight Willow Home Care Business Cards

We are looking to create double sided, sleek business cards for our new Home Health Care Agency, Harborlight Willow Home Care, located in NJ. We want to appear established, professional and at the same time, stand out with a creative and original flair. It should have a luxurious, exclusive feel to it.
The theme colors from our logo should be incorporated into the project.

Our Logo is attached.

Information to be included on the business cards:

Insert Phone Icon: (555)-204-7390
Insert Website Icon: hwhcpx.example
Insert E-mail Icon: info@hwhcpx.example

Follow us on Social Media!
Insert Facebook Icon: (I will provide the link at a later time)
Insert Instagram Icon (I will provide the link at a later time)

In regard to location, we service the areas of: Bayville
Cedarbrook
Pinedale
Dover
Hollins
Harbor Heights
Jamison
Lakeridge
Lakemont
Marlowe Township
Port Haven Beach
Rosewood
Lone Meadow
Tidewater

All all it's neighboring areas.

However, that can take up a lot of room...therefore, I had in mind to use the backside of the card to have a MAP with all these areas marked on there...in addition to listing these service locations below the map.

We want the card to appear lively and vibrant.

Please note: I will provide the potential winner with the contact's name later on in the process.

A sample idea is attached below as well.

Use your creative juices!

Good luck!

• A map of our service areas on the back of the double sided card.
Sleek design
Our logo (refer to attachment below)

```html
<!DOCTYPE html>
<html lang="en">
<head>
<meta charset="utf-8">
<title>Harborlight Willow Home Care – Business Cards</title>
<link href="https://fonts.googleapis.com/css2?family=Montserrat:wght@400;600;700&display=swap" rel="stylesheet">
<style>
  :root{
    --backdrop:#dedede;
    --card-blue:#0a4f92;
    --deep-blue:#06345f;
    --glow-blue:#3f86d6;
    --leaf-green:#8dc63f;
    --white:#ffffff;
  }
  *{box-sizing:border-box;margin:0;padding:0}
  html,body{width:1200px;height:1200px;overflow:hidden;background:var(--backdrop);font-family:"Montserrat",sans-serif}
  .card{position:absolute;left:207px;width:786px;height:449px;background:var(--card-blue);border-radius:20px;color:var(--white)}
  .card--front{top:112px}
  .card--back{top:640px}

  .brand-name{position:absolute;font-weight:600;color:var(--white);letter-spacing:.5px;text-transform:uppercase;white-space:nowrap}
  .card--front .brand-name{left:46px;top:44px;font-size:19px}

  .person{position:absolute;left:46px;top:190px}
  .person__name{font-weight:700;font-size:28px;color:var(--leaf-green);letter-spacing:1.5px;text-transform:uppercase;line-height:1.1}
  .person__role{font-size:20px;margin-top:2px}

  .contact-list{position:absolute;left:46px;list-style:none}
  .contact-list--social{top:264px}
  .contact-list--direct{top:328px}
  .contact-list li{display:flex;align-items:center;height:25.5px;font-size:21px;white-space:nowrap}
  .contact-list svg{width:16px;height:16px;margin-right:8px;flex:none}

  .emblem-area{position:absolute;left:395px;top:50px;width:348px;height:348px;border-radius:50%;
    background:radial-gradient(circle at 35% 70%,rgba(63,134,214,.55),rgba(10,79,146,0) 60%),
               linear-gradient(135deg,var(--deep-blue),var(--card-blue) 60%)}

  .back-brand{position:absolute;left:40px;top:114px;width:376px;text-align:center}
  .back-brand__dot{width:150px;height:150px;border-radius:50%;border:6px solid var(--leaf-green);margin:0 auto 14px}
  .back-brand .brand-name{position:static;font-size:19px}

  .service-areas{position:absolute;left:447px;top:38px;list-style:none}
  .service-areas li{display:flex;align-items:center;height:28.7px;font-size:21.5px;letter-spacing:.5px;white-space:nowrap}
  .service-areas li::before{content:"";width:15px;height:15px;border-radius:50%;background:var(--leaf-green);margin-right:14px}
</style>
</head>
<body>

<section class="card card--front">
  <div class="brand-name">Harborlight Willow Home Care</div>

  <div class="person">
    <div class="person__name">Jordan Avery</div>
    <div class="person__role">Director</div>
  </div>

  <ul class="contact-list contact-list--social">
    <li><svg viewBox="0 0 16 16"><circle cx="8" cy="8" r="6.5" fill="none" stroke="var(--leaf-green)" stroke-width="2"/></svg>@Icon: hwhcpx.example</li>
    <li><svg viewBox="0 0 16 16"><circle cx="8" cy="8" r="7.5" fill="var(--leaf-green)"/></svg>/Icon: hwhcpx.example</li>
  </ul>

  <ul class="contact-list contact-list--direct">
    <li><svg viewBox="0 0 16 16"><path d="M4 1.5l2.3 3-1.3 1.6c.9 2 2.5 3.6 4.5 4.6l1.6-1.3 3 2.3-1.4 2.3C7.4 13.6 2.4 8.6 1.8 3z" fill="none" stroke="var(--leaf-green)" stroke-width="1.3" stroke-linejoin="round"/></svg>(555)-204-7390</li>
    <li><svg viewBox="0 0 16 16"><rect x="1.5" y="3.5" width="13" height="9" fill="none" stroke="var(--leaf-green)" stroke-width="1.3"/><path d="M1.5 3.5L8 9l6.5-5.5" fill="none" stroke="var(--leaf-green)" stroke-width="1.3"/></svg>Icon: info@hwhcpx.example</li>
    <li><svg viewBox="0 0 16 16" fill="none" stroke="var(--leaf-green)" stroke-width="1.1"><circle cx="8" cy="8" r="6.5"/><ellipse cx="8" cy="8" rx="3" ry="6.5"/><path d="M1.5 8h13M2.5 4.8h11M2.5 11.2h11"/></svg>www.Icon: hwhcpx.example</li>
  </ul>

  <div class="emblem-area" role="img" aria-label="Large embossed brand emblem decoration in deep blue tones"></div>
</section>

<section class="card card--back">
  <div class="back-brand">
    <div class="back-brand__dot"></div>
    <div class="brand-name">Harborlight Willow Home Care</div>
  </div>

  <ul class="service-areas">
    <li>Cedarbrook</li>
    <li>Pinedale</li>
    <li>Dover</li>
    <li>Hollins</li>
    <li>Harbor Heights</li>
    <li>Jamison</li>
    <li>Lakeridge</li>
    <li>Lakemont</li>
    <li>Marlowe Township</li>
    <li>Port Haven Beach</li>
    <li>Rosewood</li>
    <li>Lone Meadow</li>
    <li>Tidewater</li>
  </ul>
</section>

</body>
</html>
```